Flyer-Design für Segelverein
Zielgruppe
Wir sind ein kleiner Berliner Segelverein im Herzen von Berlin. Unsere Zielgruppe sind wasserbegeisterte Menschen zwischen 20-50 Jahre.
Ein Eindruck über unseren Verein gibt es auf der neuen Webseite (noch im Aufbau): www.wellenrunde-kiel.de
und der alten webseite: www.wellenrundekiel.de
Aufgabenstellung
Wir benötigen den Flyer zum Anwerben neuer Mitglieder. D.h. der Flyer soll alle notwendigen Informationen beinhalten, auf das nötigste reduziert. Vom Format würden wir daher eher was kompaktes sehen (z.b. DIN lang beidseitig bedruckt). Dann könnte auf der Vorderseite die wichtigsten Informationen zum Verein stehen und auf der Rückseite Gründe, Mitglied zu werden.
Zum Verein
1972 gegründet mit dem Ziel, das Seesegeln zu fördern. Die damalige Begeisterung, gemeinsam etwas vollbringen zu können, führte in den Jahren 1975/76 zu einer Folge von Seetörns, bei der ausnahmslos Mitglieder beteiligt waren, von der Ostsee über Norwegen, England, Kanarische Inseln, Karibik über die Bermudas und Azoren wieder zurück in die Ostsee.
Warum der Verein:
- Verkehrsgünstig und zentral gelegen direkt an der Lindgasse - Sehr gut zu erreichen mit den ÖPNVs
- Einzigartiger Schwimmsteg in Berlin ohne Landzugang - Ein Ort zum Verweilen und Abschalten
- verfügbare Stegplätze für Bootsbesitzer
- Viele Vereinsboote für Mitglieder ohne Boot -
- Günstige Mitgliedsbeiträge - Studenten und Schüler erhalten Ermässigungen
- Ein familiärer kleiner Verein - Keine umfangreichen Pflichtarbeiten
- Vereinsinterne Regatten entlang der Havel
- Spannende interne Events und Ausbildungsangebote wie z.b. Fahrten mit dem Dreimast-Gaffelschooner Solvenja, Knotenkurse, Navigation

```html
<!DOCTYPE html>
<html lang="de">
<head>
<meta charset="utf-8">
<title>Wellenrunde BERLIN – Flyer</title>
<link rel="stylesheet" href="https://fonts.googleapis.com/css2?family=Krona+One&family=Questrial&family=Roboto+Condensed:wght@400&display=swap">
<style>
  :root {
    --sail-blue: #0e4f93;
    --panel-navy: #1b3a6b;
    --map-blue: #24487f;
    --signal-red: #e5291f;
    --white: #ffffff;
    --water-light: #c9d6df;
    --water-mid: #6f8ea6;
    --water-deep: #2f4f68;
    --dusk-sky: #d8d4cc;
    --deck-dark: #2a2a30;
  }
  * { margin: 0; padding: 0; box-sizing: border-box; }
  html, body { width: 1159px; height: 1200px; overflow: hidden; background: var(--white); }
  .flyer { position: relative; width: 1159px; height: 1200px; }

  .front { position: absolute; left: 0; top: 0; width: 1159px; height: 594px; overflow: hidden; }
  .front-photo {
    position: absolute; inset: 0;
    background: linear-gradient(180deg, var(--water-light) 0%, #a7bccb 35%, var(--water-mid) 65%, var(--water-deep) 100%);
  }
  .front-shapes { position: absolute; left: 0; top: 0; }
  .headline { font-family: "Krona One", sans-serif; fill: var(--white); font-size: 46px; }
  .call { font-family: "Krona One", sans-serif; fill: var(--signal-red); font-size: 34px; }

  .club-name {
    position: absolute; left: 236px; top: 212px;
    font-family: "Krona One", sans-serif; font-size: 24px; letter-spacing: 1px;
    color: var(--white); white-space: nowrap;
  }
  .reasons {
    position: absolute; left: 222px; top: 259px; list-style: none;
    font-family: "Questrial", sans-serif; font-size: 19.5px; line-height: 25px;
    letter-spacing: 1.2px; color: var(--white); white-space: nowrap;
  }
  .reasons li::before { content: "- "; }
  .contact {
    position: absolute; left: 168px; top: 482px;
    font-family: "Questrial", sans-serif; font-size: 14.5px; line-height: 19px;
    color: var(--white); white-space: nowrap; font-style: normal;
  }
  .contact .address { letter-spacing: 1px; margin-bottom: 6px; }

  .back {
    position: absolute; left: 0; top: 606px; width: 1159px; height: 594px; overflow: hidden;
  }
  .back-photo {
    position: absolute; inset: 0;
    background: linear-gradient(160deg, var(--dusk-sky) 0%, #b9b6b2 30%, #6c6f78 55%, #3d3e46 75%, var(--deck-dark) 100%);
  }
  .club-mark {
    position: absolute; right: 40px; top: 118px;
    display: flex; align-items: center; gap: 12px;
    font-family: "Krona One", sans-serif; font-size: 20px; color: var(--white);
  }
  .club-mark .dot { width: 22px; height: 22px; border-radius: 50%; background: var(--signal-red); }
  .slogan {
    position: absolute; right: 36px; top: 322px; text-align: right;
    color: var(--white); white-space: nowrap;
  }
  .slogan h2 { font-family: "Krona One", sans-serif; font-weight: 400; font-size: 37px; line-height: 50px; }
  .slogan p { font-family: "Roboto Condensed", sans-serif; font-size: 25px; line-height: 28px; }
</style>
</head>
<body>
<main class="flyer">
  <section class="front">
    <div class="front-photo" role="img" aria-label="Foto: spritzendes Wasser, Wellen im Gegenlicht"></div>
    <svg class="front-shapes" width="1159" height="594" viewBox="0 0 1159 594">
      <path class="sail" fill="var(--sail-blue)" d="M251 0 L887 0 Q920 180 952 337 Q700 120 233 89 Z"/>
      <path class="panel" fill="var(--panel-navy)" d="M211 214 Q430 150 777 251 L973 471 L979 594 L58 594 Q150 400 211 214 Z"/>
      <path class="map" role="img" aria-label="Lageplan des Vereinsgeländes am See" fill="var(--map-blue)" d="M584 494 Q610 420 640 320 Q700 290 777 251 L973 471 L960 500 Q820 520 700 490 Z"/>
      <path class="panel-wave" role="img" aria-label="Foto: Wasseroberfläche" fill="#5d7f9a" d="M337 594 Q450 490 588 483 Q780 480 887 594 Z"/>
      <path id="headline-path" fill="none" d="M272 55 Q600 90 820 200"/>
      <path id="call-path" fill="none" d="M228 145 Q520 150 745 215"/>
      <text class="headline"><textPath href="#headline-path">Klar zum Ablegen!</textPath></text>
      <text class="call"><textPath href="#call-path">Jetzt Mitglied werden!</textPath></text>
    </svg>
    <h1 class="club-name">Wellenrunde BERLIN</h1>
    <ul class="reasons">
      <li>Verkehrsgünstig und zentral gelegen</li>
      <li>einzigartiger Schwimmsteg ohne Landzugang</li>
      <li>Stegplätze für Bootsbesitzer verfügbar</li>
      <li>viele Vereinsboote</li>
      <li>günstige Mitgliedsbeiträge</li>
      <li>kleiner familiärer Verein</li>
      <li>vereinsinterne Regatten</li>
      <li>Events und Ausbildungsangebote</li>
    </ul>
    <address class="contact">
      <div class="address">Am Uferweg 12, 10999 Berlin</div>
      <div>info@wellenrunde-kiel.de</div>
      <div>www.wellenrundekiel.de</div>
      <div>+49 (030) 555 01 23</div>
    </address>
  </section>

  <section class="back">
    <div class="back-photo" role="img" aria-label="Foto: Segelyacht mit Segel und Winsch bei Abendlicht auf dem See"></div>
    <div class="club-mark"><span class="dot"></span><span>Wellenrunde BERLIN</span></div>
    <div class="slogan">
      <h2>Seemann lass das Träumen</h2>
      <p>Wellenrunde BERLIN - der Segelverein im Herzen von Berlin</p>
    </div>
  </section>
</main>
</body>
</html>
```